Menu revision for Korean Restaurant

I have posted the exact content in a word file that I would like to appear in the menu. Please apply to the template. I will be following up with prices shortly. I am in a hurry and not too picky. Thank you.

Make a menu with revisions.

Page 1: Cover Page
- Replace logo with new uploaded logo

Page 2:
Appetizers
Vegetarian Appetizers

Page 3:
BBQ Items

Page 4:
Signature Dishes

Page 5:
Bokkeum | Stir-Fry

Page 6:
Rice Bowls
Noodles
Hot Soup

Page 7:
Drinks

Target Market(s)

My customers

Industry/Entity Type

Restaurant

Requirements
Must have
• 1. Only use my menu content, template, and font.

```html
<!DOCTYPE html>
<html lang="en">
<head>
<meta charset="utf-8">
<title>Dalbit Galbi — Menu Spreads</title>
<link href="https://fonts.googleapis.com/css2?family=Russo+One&family=Crimson+Text:wght@400;700&family=Noto+Sans+KR:wght@400;500&display=swap" rel="stylesheet">
<style>
:root{
  --page:#131313;
  --canvas:#ffffff;
  --gold:#c8a24c;
  --gold-soft:#9c7f3e;
  --red:#d2262c;
  --ink:#ddd3bf;
}
*{box-sizing:border-box;margin:0;padding:0}
html,body{width:1200px;height:1200px;overflow:hidden;background:var(--canvas)}
body{position:relative;font-family:"Crimson Text",serif;color:var(--ink)}
.panel{position:absolute;width:436px;height:565px;background:var(--page);overflow:hidden}
.frame{position:absolute;inset:14px;border:1px solid var(--gold-soft);pointer-events:none}
.corner{position:absolute;width:12px;height:12px;border:1px solid var(--gold-soft);background:var(--page)}
.corner.tl{left:-6px;top:-6px}.corner.tr{right:-6px;top:-6px}
.corner.bl{left:-6px;bottom:-6px}.corner.br{right:-6px;bottom:-6px}
.content{position:absolute;left:27px;right:28px;top:22px}
.section-title{font-family:"Russo One",sans-serif;color:var(--red);font-size:22px;letter-spacing:3px;text-align:center;margin-bottom:18px;white-space:nowrap}
.items{list-style:none}
.item{display:grid;grid-template-columns:1fr 46px;column-gap:10px;margin-bottom:4px;align-items:start}
.item-text{font-size:7.5px;line-height:10px;color:var(--ink)}
.item-name{font-family:"Russo One",sans-serif;color:var(--gold);font-size:12px;letter-spacing:.6px;margin-right:4px}
.item-kr{font-family:"Noto Sans KR",sans-serif;font-size:12px;color:var(--gold);margin-right:5px}
.price{font-family:"Crimson Text",serif;font-weight:700;font-size:11.5px;color:var(--ink);text-align:right;letter-spacing:.5px;padding-top:1px}
.divider{position:relative;height:1px;background:var(--gold-soft);margin:24px 0 36px}
.divider::after{content:"";position:absolute;left:50%;top:-10px;width:20px;height:20px;margin-left:-10px;border-radius:50%;border:1px solid var(--gold);background:var(--page)}
.note{position:absolute;left:40px;bottom:16px;font-size:5.5px;color:var(--ink)}
.options{display:grid;grid-template-columns:repeat(3,1fr);font-size:7.5px;margin:6px 0 14px;color:var(--ink)}
.centerpiece{display:grid;grid-template-columns:70px 1fr;column-gap:14px;font-size:7.5px;line-height:10.5px;margin-top:12px}
.centerpiece-label{font-family:"Russo One",sans-serif;font-weight:400;color:var(--gold);font-size:9px;letter-spacing:.5px;display:block}

.cover{left:18px;top:15px}
.brand{position:absolute;left:0;right:0;top:255px;display:flex;align-items:center;justify-content:center;gap:12px}
.brand-mark{width:50px;height:50px;background:var(--red)}
.brand-name{font-family:"Russo One",sans-serif;color:var(--red);font-size:38px;letter-spacing:3px}

.bbq{left:745px;top:20px}
.appetizers{left:469px;top:17px}
.bokkeum{left:745px;top:612px}
.signature{left:387px;top:604px}
.noodles{left:18px;top:598px}

.bbq .content{left:166px;right:26px}
.bbq .item{margin-bottom:3.5px}
.bbq .item-text{line-height:9px}
.signature .content{left:74px;right:28px}
.bokkeum .content{left:88px;right:24px}
.bokkeum .section-title{font-size:20px;letter-spacing:2px}
.bokkeum .item{margin-bottom:3px}
.bokkeum .item-text{line-height:9.5px}
.bokkeum .divider{margin:18px 0 28px}
</style>
</head>
<body>

<section class="panel cover">
  <div class="frame"><span class="corner tl"></span><span class="corner tr"></span><span class="corner bl"></span><span class="corner br"></span></div>
  <div class="brand">
    <span class="brand-mark"></span>
    <span class="brand-name">DALBIT GALBI</span>
  </div>
</section>

<section class="panel bbq">
  <div class="frame"><span class="corner tl"></span><span class="corner tr"></span><span class="corner bl"></span><span class="corner br"></span></div>
  <div class="content">
    <h2 class="section-title">BBQ ITEMS</h2>
    <ul class="items">
      <li class="item"><p class="item-text"><span class="item-name">GALBI</span><span class="item-kr">갈비</span>Hand crafted beef short rib marinated in house-made.</p><span class="price">$9.95</span></li>
      <li class="item"><p class="item-text"><span class="item-name">LA GALBI</span><span class="item-kr">LA갈비</span>3-bone beef short ribs marinated in a house sauce.</p><span class="price">$9.95</span></li>
      <li class="item"><p class="item-text"><span class="item-name">SAENG GALBI</span><span class="item-kr">생갈비</span>Hand crafted beef short ribs.</p><span class="price">$9.95</span></li>
      <li class="item"><p class="item-text"><span class="item-name">SAENG LA</span><span class="item-kr">생LA</span>3-bone beef short ribs. Non-marinated</p><span class="price">$9.95</span></li>
      <li class="item"><p class="item-text"><span class="item-name">KKOT DEUNG SHIM</span><span class="item-kr">생꽃등심</span>Ribeye.</p><span class="price">$9.95</span></li>
      <li class="item"><p class="item-text"><span class="item-name">BULGOGI</span><span class="item-kr">불고기</span></p><span class="price">$9.95</span></li>
      <li class="item"><p class="item-text"><span class="item-name">CHADOL</span><span class="item-kr">차돌박이</span>Thinly sliced black angus brisket.</p><span class="price">$9.95</span></li>
      <li class="item"><p class="item-text"><span class="item-name">HYEOMIT</span><span class="item-kr">혀밑구이</span>Beef Tongue</p><span class="price">$9.95</span></li>
      <li class="item"><p class="item-text"><span class="item-name">SAMGYUP</span><span class="item-kr">삼겹살</span>Pork Belly</p><span class="price">$9.95</span></li>
      <li class="item"><p class="item-text"><span class="item-name">HEUK SAMGYEOPSAL</span><span class="item-kr">흑돼지삼겹살</span>Jeju Black</p><span class="price">$9.95</span></li>
      <li class="item"><p class="item-text"><span class="item-name">HANG JUNG</span><span class="item-kr">항정살</span>Pork Jowl</p><span class="price">$9.95</span></li>
      <li class="item"><p class="item-text"><span class="item-name">MOKSAL</span><span class="item-kr">목살</span></p><span class="price">$9.95</span></li>
      <li class="item"><p class="item-text"><span class="item-name">DAEPAE</span><span class="item-kr">대패</span></p><span class="price">$9.95</span></li>
      <li class="item"><p class="item-text"><span class="item-name">JUKKUMI</span><span class="item-kr">쭈꾸미</span>Baby Octopus</p><span class="price">$9.95</span></li>
      <li class="item"><p class="item-text"><span class="item-name">UDON</span><span class="item-kr">우동</span>sari</p><span class="price">$9.95</span></li>
      <li class="item"><p class="item-text"><span class="item-name">SEWOO</span><span class="item-kr">새우</span></p><span class="price">$9.95</span></li>
      <li class="item"><p class="item-text"><span class="item-name">YACHAE</span><span class="item-kr">야채구이</span>Assorted Vegetables</p><span class="price">$9.95</span></li>
      <li class="item"><p class="item-text"><span class="item-name">FILET</span><span class="item-kr">안심</span>Filet mignon marinated in garlic-soy marinate</p><span class="price">$9.95</span></li>
      <li class="item"><p class="item-text"><span class="item-name">DAK</span><span class="item-kr">닭고기</span>Boneless chicken breast. Marinated in house sauce.</p><span class="price">$9.95</span></li>
      <li class="item"><p class="item-text"><span class="item-name">DWAEJI</span><span class="item-kr">돼지불고기</span>Pork loin marinated with house sauce.</p><span class="price">$9.95</span></li>
    </ul>
  </div>
</section>

<section class="panel appetizers">
  <div class="frame"><span class="corner tl"></span><span class="corner tr"></span><span class="corner bl"></span><span class="corner br"></span></div>
  <div class="content">
    <h2 class="section-title">APPETIZERS</h2>
    <ul class="items">
      <li class="item"><p class="item-text"><span class="item-name">MANDU</span><span class="item-kr">군만두</span></p><span class="price">$9.95</span></li>
      <li class="item"><p class="item-text"><span class="item-name">MUL MANDU</span><span class="item-kr">물만두</span></p><span class="price">$9.95</span></li>
      <li class="item"><p class="item-text"><span class="item-name">CHICKEN WINGS</span><span class="item-kr">닭날개</span></p><span class="price">$9.95</span></li>
      <li class="item"><p class="item-text"><span class="item-name">SPICY WINGS</span><span class="item-kr">닭날개</span></p><span class="price">$9.95</span></li>
      <li class="item"><p class="item-text"><span class="item-name">YANG YUM CHICKEN</span><span class="item-kr">양념치킨</span></p><span class="price">$9.95</span></li>
      <li class="item"><p class="item-text"><span class="item-name">SHRIMP TEMPURA</span><span class="item-kr">새우튀김</span></p><span class="price">$9.95</span></li>
      <li class="item"><p class="item-text"><span class="item-name">FRIED CALAMARI</span><span class="item-kr">오징어튀김</span></p><span class="price">$9.95</span></li>
      <li class="item"><p class="item-text"><span class="item-name">HAEMUL PAJEON</span><span class="item-kr">해물파전</span>Assortment of fresh calamari, shrimp, scallops, mussels, and scallions in a Korean pancake.</p><span class="price">$9.95</span></li>
    </ul>
    <div class="divider" style="margin-top:52px"></div>
    <h2 class="section-title">VEGETARIAN APPETIZERS</h2>
    <ul class="items">
      <li class="item"><p class="item-text"><span class="item-name">VEGGIE MANDU</span><span class="item-kr">야채만두</span></p><span class="price">$9.95</span></li>
      <li class="item"><p class="item-text"><span class="item-name">VEGGIE MUL MANDU</span><span class="item-kr">야채물만두</span></p><span class="price">$9.95</span></li>
      <li class="item"><p class="item-text"><span class="item-name">SWEET POTATO TEMPURA</span><span class="item-kr">고구마튀김</span></p><span class="price">$9.95</span></li>
      <li class="item"><p class="item-text"><span class="item-name">VEGGIE TEMPURA</span><span class="item-kr">야채튀김</span></p><span class="price">$9.95</span></li>
      <li class="item"><p class="item-text"><span class="item-name">MUSHROOM TEMPURA</span><span class="item-kr">버섯튀김</span></p><span class="price">$9.95</span></li>
      <li class="item"><p class="item-text"><span class="item-name">PAJEON</span><span class="item-kr">파전</span>Pan fried green onion pancake</p><span class="price">$9.95</span></li>
      <li class="item"><p class="item-text"><span class="item-name">HOBAK GOCHU JEON</span><span class="item-kr">호박고추전</span>Zucchini and Jalapeño pancake</p><span class="price">$9.95</span></li>
      <li class="item"><p class="item-text"><span class="item-name">KIMCHI PAJEON</span><span class="item-kr">김치파전</span>Crispy kimchi and scallion pancake</p><span class="price">$9.95</span></li>
    </ul>
  </div>
  <p class="note">* Jeon batter contains wheat flour &amp; eggs.</p>
</section>

<section class="panel bokkeum">
  <div class="frame"><span class="corner tl"></span><span class="corner tr"></span><span class="corner bl"></span><span class="corner br"></span></div>
  <div class="content">
    <h2 class="section-title">BOKKEUM | STIR-FRY</h2>
    <ul class="items">
      <li class="item"><p class="item-text"><span class="item-name">JEYUK BOKKEUM</span><span class="item-kr">제육볶음</span>Pork, onions, scallions, mushrooms stir-fried in a spicy red garlic sauce</p><span class="price">$9.95</span></li>
      <li class="item"><p class="item-text"><span class="item-name">DUBU BOKKEUM (V)</span><span class="item-kr">두부볶음</span>Fried tofu cubes, zucchini, onions, and mushrooms stir-fried in a red chili sauce</p><span class="price">$9.95</span></li>
      <li class="item"><p class="item-text"><span class="item-name">KIMCHI BOKKEUM</span><span class="item-kr">김치볶음</span>Pork, kimchi, rice cakes, scallions, with fresh tofu</p><span class="price">$9.95</span></li>
      <li class="item"><p class="item-text"><span class="item-name">HAEMUL BOKKEUM</span><span class="item-kr">해물볶음</span>Jumbo shrimp, scallops, mussels, octopus, zucchini, carrots, onions, scallions, mushrooms, and jalapenos</p><span class="price">$9.95</span></li>
      <li class="item"><p class="item-text"><span class="item-name">SAMGYUPSAL BOKKEUM</span><span class="item-kr">매운삼겹살</span>Pork belly, zucchini, onions stir-fried in a spicy gochu wine sauce</p><span class="price">$9.95</span></li>
      <li class="item"><p class="item-text"><span class="item-name">OJINGEO BOKKEUM</span><span class="item-kr">오징어볶음</span>Fresh calamari stir-fried with zucchini, mushrooms, onions and scallions in a hot and spicy chili</p><span class="price">$9.95</span></li>
      <li class="item" style="margin-top:6px"><p class="item-text"><span class="item-name">NAKJI BOKKEUM</span><span class="item-kr">낙지볶음</span>Fresh octopus stir-fried with carrots, mushrooms, onions, and scallions in a hot and spicy chili sauce</p><span class="price">$9.95</span></li>
      <li class="item"><p class="item-text"><span class="item-name">JUKKUMI SAMGYUPSAL</span><span class="item-kr">쭈꾸미삼겹살</span>Spicy pork belly with baby octopus</p><span class="price">$9.95</span></li>
    </ul>
    <div class="divider"></div>
    <h2 class="section-title">RICE BOWL</h2>
    <ul class="items">
      <li class="item"><p class="item-text"><span class="item-name">YUKHWE BIBIMBAP</span><span class="item-kr">육회비빔밥</span>Raw beef tartar &amp; egg yolk atop a colorful spread of spinach, carrots, bean sprouts, soybean sprouts, shiitake mushrooms, zucchini, and radish. Topped with garlic and pine nuts and served with a side of house-made gochujang &amp; bowl of rice.</p><span class="price">$9.95</span></li>
      <li class="item"><p class="item-text"><span class="item-name">DOLSOT BIBIMBAP</span><span class="item-kr">돌솥비빔밥</span>Sizzling hot stone bowl with individually marinated spinach, carrots, bean sprouts, soybean sprouts, mushrooms, zucchini, and radish topped with choice of fried egg or yolk. Served with a side of house-made gochujang sauce.</p><span class="price">$9.95</span></li>
    </ul>
    <div class="centerpiece">
      <div class="item-text"><span class="centerpiece-label">ADD-ONS:</span>Gochujang</div>
      <div class="item-text"><span class="centerpiece-label">CHOOSE CENTERPIECE:</span>Tofu or Kimchi:<br>Bulgogi (original) or Chicken:<br>Kimchi &amp; Pork:<br>Seafood:</div>
    </div>
  </div>
</section>

<section class="panel signature">
  <div class="frame"><span class="corner tl"></span><span class="corner tr"></span><span class="corner bl"></span><span class="corner br"></span></div>
  <div class="content">
    <h2 class="section-title">SIGNATURE DISHES</h2>
    <ul class="items">
      <li class="item"><p class="item-text"><span class="item-name">DWAEJI BOSSAM</span><span class="item-kr">돼지보쌈</span>Braised pork belly wraps accompanied with spicy gochu &amp; oyster-pureed radish salad. Served with fresh garlic &amp; jalapeno slices, a side of salty shrimp sauce, and a side of house made ssam-jang paste with choice of boiled Napa cabbage wrap or fresh lettuce wrap</p><span class="price">$9.95</span></li>
      <li class="item"><p class="item-text"><span class="item-name">YUK-HWE</span><span class="item-kr">육회</span>Raw sesame steak tartar &amp; egg yolk. Julienned strips of lean beef seasoned and dressed with Korean pear, garlic, &amp; pine nuts</p><span class="price">$9.95</span></li>
      <li class="item"><p class="item-text"><span class="item-name">DON KATSU</span><span class="item-kr">돈까스</span>Pork loin breaded in seasoned panko crust &amp; fried. Dressed with bold katsu sauce and served with radish condiments</p><span class="price">$9.95</span></li>
      <li class="item"><p class="item-text"><span class="item-name">CHICKEN KATSU</span><span class="item-kr">치킨까스</span>Chicken breast breaded in seasoned panko crust &amp; deep-fried. Dressed with bold katsu sauce and served with radish condiments</p><span class="price">$9.95</span></li>
      <li class="item"><p class="item-text"><span class="item-name">SWEET &amp; SOUR PORK</span><span class="item-kr">탕수육</span>Pork tenderloin fried in a light batter. Served with fresh vegetables and pineapples. Drizzled with house made sweet &amp; sour sauce</p><span class="price">$9.95</span></li>
      <li class="item"><p class="item-text"><span class="item-name">SWEET &amp; SOUR CHICKEN</span><span class="item-kr">탕수치킨</span>Tender pieces of all white chicken breast fried in a light batter. Served with fresh vegetables and pineapples. Drizzled with house made sweet &amp; sour sauce</p><span class="price">$9.95</span></li>
      <li class="item"><p class="item-text"><span class="item-name">SWEET &amp; SOUR SHRIMP</span><span class="item-kr">탕수새우</span>A generous portion of shrimp fried in a light batter. Served with fresh vegetables and pineapples. Drizzled with house made sweet &amp; sour sauce</p><span class="price">$9.95</span></li>
      <li class="item"><p class="item-text"><span class="item-name">BULGOGI-IN-A-BOWL</span><span class="item-kr">뚝배기불고기</span>Bulgogi, vermicelli, enoki, shiitake mushrooms, scallions, onions, &amp; carrot garnish all in one bowl &amp; filled to the brim with a hearty bulgogi broth</p><span class="price">$9.95</span></li>
      <li class="item"><p class="item-text"><span class="item-name">GOPCHANG GUI</span><span class="item-kr">곱창구이</span>Sizzling beef chitterlings with tripe and a medley spiced with wild sesame and red pepper oil</p><span class="price">$9.95</span></li>
      <li class="item"><p class="item-text"><span class="item-name">GRILLED MACKEREL</span><span class="item-kr">고등어구이</span>Whole bone-in silver belly chub mackerel salted and seared.</p><span class="price">$9.95</span></li>
    </ul>
  </div>
</section>

<section class="panel noodles">
  <div class="frame"><span class="corner tl"></span><span class="corner tr"></span><span class="corner bl"></span><span class="corner br"></span></div>
  <div class="content">
    <h2 class="section-title">NOODLE DISHES</h2>
    <ul class="items">
      <li class="item"><p class="item-text"><span class="item-name">MUL NAENG MYUN</span><span class="item-kr">물냉면</span>Beef brisket, pickled radish, cucumbers slices, jalapenos, and hard-boiled egg layered on top of thin buckwheat noodles in icy beef broth.</p><span class="price">$9.95</span></li>
      <li class="item"><p class="item-text"><span class="item-name">BIBIM NAENG MYUN</span><span class="item-kr">비빔냉면</span>Pickled radish, cucumber slices, jalapenos, scallions, and hard-boiled egg set atop a mound of sweet &amp; spicy buckwheat noodles.</p><span class="price">$9.95</span></li>
    </ul>
    <div class="divider" style="margin-top:34px;margin-bottom:56px"></div>
    <h2 class="section-title">HOT SOUP</h2>
    <ul class="items">
      <li class="item"><p class="item-text"><span class="item-name">*SOON DUBU CHIGAE</span><span class="item-kr">순두부찌개</span>Soft tofu stew with mushrooms, egg, and choice of protein in boiling spicy chili oil broth</p><span class="price">$9.95</span></li>
    </ul>
    <div class="options"><span>Vegetarian</span><span style="text-align:center">Beef, Chicken, or Pork</span><span style="text-align:right;padding-right:60px">Seafood</span></div>
    <ul class="items">
      <li class="item"><p class="item-text"><span class="item-name">KIMCHI CHIGAE</span><span class="item-kr">김치찌개</span>Kimchi, pork, tofu, fish cake, scallions, mushrooms and spicy pepper flakes in boiling kimchi broth</p><span class="price">$9.95</span></li>
      <li class="item"><p class="item-text"><span class="item-name">GALBI TANG</span><span class="item-kr">갈비탕</span>Beef short rib soup with radishes, mushrooms, scallions, vermicelli noodles</p><span class="price">$9.95</span></li>
    </ul>
  </div>
</section>

</body>
</html>
```